Toronto based company needs a logo and business card design

We are "Brellmont Restoration Corp.". A high rise building restoration company based in Toronto. We specialize in Building Envelope, Parking Garage and Waterproofing repairs. Would like to see designs which use the color Teal, Black and White or Red, Black and White. Prefer to have light color background for the front of the card and dark background for the reverse side. For logo design, we would prefer to see high rise building/s incorporated in it.

Industry/Entity Type

Construction

Logo Text

Brellmont

Font styles to use
Sans Serif

Colors
00a990
ffffff
ec1f27
85acd3
000000

```html
<!DOCTYPE html>
<html lang="en">
<head>
<meta charset="utf-8">
<title>Brellmont Restoration Corp. – Business Card</title>
<link rel="stylesheet" href="https://fonts.googleapis.com/css2?family=Open+Sans:wght@400;600;700&display=swap">
<style>
  :root {
    --backdrop: #3b322d;
    --card-light: #f7f7f6;
    --card-dark: #0c0c0c;
    --ink: #222222;
    --ink-soft: #555555;
    --rule: #bdbdbd;
    --accent: #ec1f27;
    --white: #ffffff;
  }
  * { box-sizing: border-box; margin: 0; padding: 0; }
  html, body {
    width: 1200px; height: 844px; overflow: hidden;
    background: var(--backdrop);
    font-family: "Open Sans", Arial, sans-serif;
  }
  .canvas { position: relative; width: 1200px; height: 844px; }
  .card {
    position: absolute; top: 279px;
    width: 510px; height: 292px;
    box-shadow: 0 14px 30px rgba(0,0,0,.45);
  }
  .card--front { left: 70px; background: var(--card-light); color: var(--ink); }
  .card--back  { left: 620px; background: var(--card-dark); color: var(--white); }

  .brand { display: flex; align-items: center; gap: 8px; }
  .brand__dot { width: 12px; height: 12px; border-radius: 50%; background: var(--accent); flex: none; }
  .brand__name { font-weight: 400; letter-spacing: .06em; text-transform: uppercase; line-height: 1.15; }

  .card--front .brand { position: absolute; right: 34px; top: 48px; }
  .card--front .brand__name { font-size: 20px; color: var(--ink); text-align: left; }

  .card--front .rule { position: absolute; left: 34px; right: 34px; height: 1px; background: var(--rule); }
  .rule--top { top: 126px; }
  .rule--bottom { top: 222px; }

  .person { position: absolute; left: 34px; top: 142px; }
  .person__name { font-weight: 700; font-size: 17px; color: var(--accent); letter-spacing: .03em; text-transform: uppercase; }
  .person__role { font-size: 13px; color: var(--ink-soft); margin-top: 1px; }
  .person__address { font-size: 13px; color: var(--ink); margin-top: 10px; }

  .contact { position: absolute; left: 34px; top: 232px; font-size: 12.5px; color: var(--ink); line-height: 1.6; }
  .contact__label { color: var(--accent); }
  .contact__row span + span { margin-left: 10px; }
  .contact__web { color: var(--accent); }

  .card--back .brand { position: absolute; left: 50%; top: 50%; transform: translate(-50%, -50%); }
  .card--back .brand__name { font-size: 26px; color: var(--white); text-align: center; }
</style>
</head>
<body>
<main class="canvas">
  <section class="card card--front" aria-label="Card front">
    <div class="brand">
      <span class="brand__dot"></span>
      <span class="brand__name">Brellmont<br>Restoration Corp.</span>
    </div>
    <div class="rule rule--top"></div>
    <div class="person">
      <p class="person__name">Daniel Marsh</p>
      <p class="person__role">Managing Director</p>
      <p class="person__address">480 Harbourview Ave, Toronto, ON M5V 2K8</p>
    </div>
    <div class="rule rule--bottom"></div>
    <div class="contact">
      <p class="contact__row">
        <span><span class="contact__label">T:</span>(416) 555 0142</span>
        <span><span class="contact__label">F:</span>(416) 555 0143</span>
        <span><span class="contact__label">M:</span>(416) 555 0144</span>
      </p>
      <p class="contact__row">
        <span><span class="contact__label">E:</span>info@brellmontcorp.ca</span>
        <span class="contact__web">www.brellmontcorp.ca</span>
      </p>
    </div>
  </section>

  <section class="card card--back" aria-label="Card back">
    <div class="brand">
      <span class="brand__dot"></span>
      <span class="brand__name">Brellmont<br>Restoration Corp.</span>
    </div>
  </section>
</main>
</body>
</html>
```